Natural Stone Company Redesign

Looking for a fresh, creative, website design. We service Luxury Residential projects in US and Internationally. We would like to see a design that communicates a passion for creative challenging design that is merged with natural stone projects. Our new company Logo is "Stoneward Atelier"

We like to emphasis from concept to completion, for example, photos of blueprints and/or sketches of a project, then a completion photo of same project.

some websites we like are:
http://www.fernbrockhale.com/
http://lontavimarchitects.com/

We would like to highlight our services of "concept to completion" scenario. Blueprints/sketches to finished products.
Page needed:
Home
About Us
Projects
Contact Us

Target Market(s)

Developers, architects, designers

Industry/Entity Type

It Company

Number of Pages Required

4 page

Font styles to use
Sans Serif

Requirements
Must have
• "Stoneward Atelier"
• New, innovative, look.
• Something to grab the attention, and make them think
Nice to have
• Motion on the homepage
• Roll over the finished project photo, and have the name of the stone pop up

```html
<!DOCTYPE html>
<html lang="en">
<head>
<meta charset="utf-8">
<title>About us · Stoneward Atelier</title>
<link rel="stylesheet" href="https://fonts.googleapis.com/css2?family=Poppins:wght@200;300;400;500&family=Roboto:ital,wght@0,400;0,500;1,400&display=swap">
<style>
  :root {
    --ink: #222428;
    --text: #4a4d55;
    --muted: #8b8f99;
    --accent: #f58634;
    --band: #f3f3f3;
    --white: #ffffff;
    --footer: #262a3a;
    --footer-text: #a8acb8;
    --footer-line: #3b4052;
  }
  * { box-sizing: border-box; margin: 0; padding: 0; }
  html, body { width: 1200px; height: 2365px; overflow: hidden; }
  body { position: relative; background: var(--white); font-family: "Roboto", Arial, sans-serif; color: var(--text); }
  .abs { position: absolute; }

  .site-header { position: absolute; left: 0; top: 0; width: 1200px; height: 77px; background: var(--white); }
  .brand { position: absolute; left: 88px; top: 24px; font-family: "Poppins", sans-serif; font-weight: 400; font-size: 22px; color: var(--ink); }
  .menu-toggle { position: absolute; left: 1092px; top: 28px; }

  .page-hero { position: absolute; left: 0; top: 77px; width: 1200px; height: 196px;
    background: linear-gradient(180deg, #6f7279 0%, #7d7f84 45%, #55575e 100%); }
  .page-hero .tint { position: absolute; left: 0; top: 0; width: 1200px; height: 196px;
    background: linear-gradient(90deg, rgba(60,62,68,.35) 0%, rgba(120,118,112,.25) 40%, rgba(70,72,80,.45) 100%); }
  .page-title { position: absolute; left: 0; width: 1200px; top: 66px; text-align: center;
    font-family: "Poppins", sans-serif; font-weight: 300; font-size: 35px; color: var(--white); }
  .breadcrumb { position: absolute; left: 0; width: 1200px; top: 122px; text-align: center;
    font-size: 12px; color: var(--white); }
  .breadcrumb .sep { margin: 0 10px; font-size: 10px; }

  .sec-num { position: absolute; font-family: "Poppins", sans-serif; font-weight: 200; font-size: 40px; color: var(--ink); line-height: 1; }
  .sec-title { position: absolute; border-left: 2px solid var(--accent); padding-left: 24px;
    font-family: "Poppins", sans-serif; font-weight: 300; font-size: 25px; line-height: 36px; color: var(--ink); }
  .sec-copy { position: absolute; width: 414px; font-size: 13px; line-height: 27px; color: var(--text); text-align: justify; }

  .photo { position: absolute; box-shadow: 0 30px 40px -18px rgba(0,0,0,.28); }
  .photo-modern-house { left: 600px; top: 349px; width: 512px; height: 351px;
    background: linear-gradient(180deg, #6aa6de 0%, #a9cdee 40%, #d9dde2 55%, #3b3e44 85%, #5a4a3a 100%); }
  .photo-courtyard-house { left: 88px; top: 793px; width: 512px; height: 352px;
    background: linear-gradient(180deg, #8fb0cf 0%, #dfe3e4 45%, #d8d1c4 62%, #3d3a36 78%, #5d7a3a 100%); }

  .testimonial-band { position: absolute; left: 0; top: 1235px; width: 1200px; height: 350px; background: var(--band); }
  .divider-v { position: absolute; left: 446px; top: 1333px; width: 1px; height: 157px; background: #d8d8d8; }
  .quote-mark { position: absolute; font-family: "Poppins", sans-serif; font-weight: 500; font-size: 62px; line-height: 1; color: #d4d4d4; }
  .quote-text { position: absolute; left: 522px; top: 1354px; width: 490px; font-size: 13px; line-height: 31px; color: var(--text); }
  .quote-author { position: absolute; left: 522px; top: 1462px; font-size: 12px; font-weight: 500; letter-spacing: .6px; color: var(--ink); }
  .quote-author::before { content: ""; display: inline-block; width: 35px; height: 1px; background: #b9b9b9; vertical-align: middle; margin-right: 12px; }
  .slider-dots { position: absolute; left: 1104px; top: 1395px; }
  .slider-dots span { display: block; width: 5px; height: 5px; border-radius: 50%; background: #b5b5b5; margin-bottom: 5px; }

  .member-card { position: absolute; top: 1690px; width: 246px; height: 270px; overflow: hidden; }
  .member-card .shade { position: absolute; left: 0; bottom: 0; width: 100%; height: 130px;
    background: linear-gradient(180deg, rgba(0,0,0,0) 0%, rgba(0,0,0,.45) 100%); }
  .member-name { position: absolute; left: 0; width: 100%; text-align: center; font-family: "Poppins", sans-serif; font-size: 19px; color: var(--white); }
  .member-role { position: absolute; left: 0; width: 100%; text-align: center; font-size: 12px; font-style: italic; color: #e8e8e8; }
  .card-faded { left: -169px; background: linear-gradient(180deg, #9a958a 0%, #b5ad9d 60%, #8b857a 100%); opacity: .85; }
  .card-one { left: 88px; background: linear-gradient(180deg, #3a3c3e 0%, #6c5a4a 45%, #7a4a52 80%, #4d3a3c 100%); }
  .card-two { left: 347px; background: linear-gradient(180deg, #3c4a44 0%, #2f3d40 50%, #233440 100%); box-shadow: 0 28px 36px -14px rgba(0,0,0,.4); }
  .card-two .shade { height: 160px; background: linear-gradient(180deg, rgba(20,40,55,0) 0%, rgba(20,40,55,.75) 100%); }
  .card-three { left: 604px; background: linear-gradient(180deg, #e0b04a 0%, #d9a646 50%, #c4a06a 100%); }
  .social { position: absolute; top: 1902px; width: 22px; height: 22px; border-radius: 50%; background: rgba(255,255,255,.2); }

  .site-footer { position: absolute; left: 0; top: 2058px; width: 1200px; height: 307px; background: var(--footer); }
  .foot-heading { position: absolute; top: 2128px; font-family: "Poppins", sans-serif; font-weight: 400; font-size: 17px; color: var(--white); }
  .foot-heading::after { content: ""; position: absolute; left: 0; top: 30px; width: 18px; height: 2px; background: var(--accent); }
  .foot-item { position: absolute; font-size: 12px; color: var(--footer-text); }
  .foot-link { position: absolute; left: 530px; font-size: 12px; color: var(--footer-text); }
  .foot-link::before { content: "›"; margin-right: 5px; }
  .newsletter-field { position: absolute; left: 793px; top: 2182px; width: 319px; height: 30px; border-bottom: 1px solid #c9ccd4; font-size: 13px; color: var(--footer-text); }
  .newsletter-send { position: absolute; left: 793px; top: 2230px; width: 44px; height: 25px; border-radius: 13px; background: var(--accent); }
  .foot-rule { position: absolute; left: 88px; top: 2312px; width: 1024px; height: 1px; background: var(--footer-line); }
  .copyright { position: absolute; left: 88px; top: 2332px; font-size: 12px; color: var(--white); }
  .to-top { position: absolute; left: 1136px; top: 2292px; width: 40px; height: 40px; border-radius: 50%; background: #3e4354; }
</style>
</head>
<body>

<header class="site-header">
  <div class="brand">Stoneward Atelier</div>
  <svg class="menu-toggle" width="20" height="18" viewBox="0 0 20 18">
    <rect x="0" y="2" width="20" height="2" fill="#222428"/>
    <rect x="0" y="8" width="20" height="2" fill="#222428"/>
    <rect x="0" y="14" width="20" height="2" fill="#222428"/>
  </svg>
</header>

<section class="page-hero" role="img" aria-label="Photo of a modern flat-roofed stone house at dusk">
  <div class="tint"></div>
  <h1 class="page-title">About us</h1>
  <div class="breadcrumb">HOME<span class="sep">›</span>ABOUT US</div>
</section>

<div class="sec-num" style="left:88px; top:393px;">01</div>
<h2 class="sec-title" style="left:88px; top:453px;">Our History<br>Introduction</h2>
<p class="sec-copy" style="left:88px; top:553px;">Quisque rutruma aenean imperdiet etiam ultricies nisi vel augue cura bitur ullamcorper ultricies nisi. Nam eget dui etiam rhoncus maece nas tempus tellus eget condimentum rhoncus sem quam semper libero sit amet adipiscing sem neque sed ipsum nam quam nunc blan dit vel luctus pulvinar hendrerit id lorem.</p>
<div class="photo photo-modern-house" role="img" aria-label="Photo of a white modern multi-storey house with dark window frames and glass balconies"></div>

<div class="photo photo-courtyard-house" role="img" aria-label="Photo of a single-storey courtyard house with lounge chairs on a terrace and lawn"></div>
<div class="sec-num" style="left:699px; top:836px;">02</div>
<h2 class="sec-title" style="left:699px; top:897px;">Our Vision<br>&amp; Missions</h2>
<p class="sec-copy" style="left:699px; top:997px;">Quisque rutruma aenean imperdiet etiam ultricies nisi vel augue cura bitur ullamcorper ultricies nisi. Nam eget dui etiam rhoncus maece nas tempus tellus eget condimentum rhoncus sem quam semper libero sit amet adipiscing sem neque sed ipsum nam quam nunc blan dit vel luctus pulvinar hendrerit id lorem.</p>

<section class="testimonial-band"></section>
<div class="sec-num" style="left:88px; top:1344px;">03</div>
<h2 class="sec-title" style="left:88px; top:1404px;">Checkout<br>What our Clients see</h2>
<div class="divider-v"></div>
<div class="quote-mark" style="left:474px; top:1330px;">“</div>
<p class="quote-text">Cras dapibus vivamus elementum semper nisi aenean vulputate eleifend tellus aenean leo ligula porttitor eu consequat vitae eleifend ac enim aliquam lorem ante dapibus in viverra quis feugiat a tellu.</p>
<div class="quote-mark" style="left:798px; top:1420px;">”</div>
<div class="quote-author">MARA ELLISON</div>
<div class="slider-dots"><span></span><span></span><span></span></div>

<div class="member-card card-faded" role="img" aria-label="Team member portrait">
  <div class="shade"></div>
  <div class="member-name" style="top:197px;">Member name</div>
</div>
<div class="member-card card-one" role="img" aria-label="Team member portrait outdoors in a crowd">
  <div class="shade"></div>
  <div class="member-name" style="top:201px;">Member name</div>
  <div class="member-role" style="top:229px;">Designation here</div>
</div>
<div class="member-card card-two" role="img" aria-label="Team member portrait among autumn foliage">
  <div class="shade"></div>
  <div class="member-name" style="top:147px;">Member name</div>
  <div class="member-role" style="top:175px;">Designation here</div>
</div>
<span class="social" style="left:407px;"></span>
<span class="social" style="left:442px;"></span>
<span class="social" style="left:476px;"></span>
<span class="social" style="left:509px;"></span>
<div class="member-card card-three" role="img" aria-label="Team member portrait against a yellow wall">
  <div class="shade"></div>
  <div class="member-name" style="top:201px;">Member name</div>
  <div class="member-role" style="top:229px;">Designation here</div>
</div>
<div class="sec-num" style="left:897px; top:1759px;">04</div>
<h2 class="sec-title" style="left:897px; top:1818px;">Our Team<br>Meet the team</h2>

<footer class="site-footer"></footer>
<h3 class="foot-heading" style="left:88px;">Location &amp; Contact Info</h3>
<svg class="abs" style="left:88px; top:2181px;" width="10" height="13" viewBox="0 0 10 13"><path d="M5 0a5 5 0 0 0-5 5c0 3.5 5 8 5 8s5-4.5 5-8a5 5 0 0 0-5-5zm0 7a2 2 0 1 1 0-4 2 2 0 0 1 0 4z" fill="#f58634"/></svg>
<div class="foot-item" style="left:106px; top:2180px;">Some address line goes here, City name, Country name.</div>
<svg class="abs" style="left:88px; top:2210px;" width="11" height="11" viewBox="0 0 11 11"><path d="M2.2 0l2 2.6-1.2 1.5a7 7 0 0 0 3.9 3.9l1.5-1.2L11 8.8 9.6 11C4.3 11 0 6.7 0 1.4z" fill="#f58634"/></svg>
<div class="foot-item" style="left:106px; top:2208px;">123 546 7890</div>
<svg class="abs" style="left:88px; top:2238px;" width="11" height="9" viewBox="0 0 11 9"><rect width="11" height="9" rx="1" fill="#f58634"/><path d="M0.5 1l5 3.6 5-3.6" stroke="#262a3a" fill="none"/></svg>
<div class="foot-item" style="left:106px; top:2235px;">info@email.com</div>

<h3 class="foot-heading" style="left:530px;">Useful Links</h3>
<div class="foot-link" style="top:2180px;">Home</div>
<div class="foot-link" style="top:2202px;">Privacy Policy</div>
<div class="foot-link" style="top:2224px;">Terms &amp; Conditions</div>

<h3 class="foot-heading" style="left:793px;">Newsletter</h3>
<div class="newsletter-field">Enter your email address...</div>
<div class="newsletter-send">
  <svg class="abs" style="left:16px; top:6px;" width="13" height="13" viewBox="0 0 13 13"><path d="M13 0L0 5.5l4.5 1.8L11 2 5.5 8.2V13l2.5-3.2 3 1.7z" fill="#ffffff"/></svg>
</div>
<div class="foot-rule"></div>
<div class="copyright">© 2017, All Rights Reserved.</div>
<div class="to-top">
  <svg class="abs" style="left:15px; top:13px;" width="10" height="14" viewBox="0 0 10 14"><path d="M5 1v12M1.5 4.5L5 1l3.5 3.5" stroke="#ffffff" stroke-width="1.2" fill="none"/></svg>
</div>

</body>
</html>
```